Visitenkarten-Design für Versicherungsmakler
Zielgruppe
Wir sind ein Versicherungsmakler aus Leipzig.
Aufgabenstellung
Im Anhang finden Sie die alte Visitenkarte. Die Daten können übernommen werden. Aber statt Inhaber bitte 'Geschäftsführer'
Die Farben sollten beibehalten werden. Bei der Frage ob das rot oder das grau die Primärfarbe ist, bin ich flexibel. Von der Gestaltung her sind Ihnen ansonsten keine Grenzen gesetzt.

```html
<!DOCTYPE html>
<html lang="de">
<head>
<meta charset="utf-8">
<title>Kaldora Finance Consulting – Visitenkarte</title>
<link rel="stylesheet" href="https://fonts.googleapis.com/css2?family=Roboto:wght@300;400;500&display=swap">
<style>
  :root {
    --stage: #7a1a1f;
    --brand-red: #d3262d;
    --brand-red-deep: #a71d25;
    --brand-red-dark: #8c1a20;
    --card-white: #f7f7f5;
    --ink: #2f2f2f;
    --ink-soft: #555555;
    --grey: #6d6d6d;
    --back-text: #e9d6d7;
  }
  * { box-sizing: border-box; margin: 0; padding: 0; }
  html, body {
    width: 1200px; height: 977px; overflow: hidden;
    background: var(--stage);
    font-family: "Roboto", Arial, sans-serif;
  }
  .stage {
    position: relative; width: 1200px; height: 977px;
    display: flex; flex-direction: column; align-items: center; justify-content: center;
    gap: 57px;
  }
  .card {
    position: relative; width: 620px; height: 400px; overflow: hidden;
    border-radius: 4px;
    box-shadow: 0 14px 34px rgba(0,0,0,0.35);
  }
  /* Front */
  .card--front { background: var(--card-white); color: var(--ink); }
  .card__band { position: absolute; left: 0; bottom: 0; width: 620px; height: 120px; }
  .brand { position: absolute; left: 56px; top: 44px; }
  .brand__name {
    font-size: 50px; font-weight: 400; color: var(--brand-red);
    letter-spacing: 1px; line-height: 1;
  }
  .brand__tagline {
    margin-top: 8px; font-size: 17px; font-weight: 400; color: var(--grey);
    letter-spacing: 1.2px;
  }
  .person { position: absolute; left: 74px; top: 178px; }
  .person__name { font-size: 27px; font-weight: 400; color: var(--ink); }
  .person__role { margin-top: 8px; font-size: 15px; font-weight: 300; color: var(--ink-soft); }
  .contact { position: absolute; left: 344px; top: 92px; font-size: 15px; color: var(--ink-soft); line-height: 1.55; }
  .contact__address { margin-bottom: 12px; font-weight: 300; }
  .contact__list { display: grid; grid-template-columns: 48px auto; column-gap: 8px; }
  .contact__label { font-weight: 500; color: var(--ink); }
  .contact__value { font-weight: 300; }
  /* Back */
  .card--back { background: var(--brand-red-dark); color: var(--back-text); }
  .card__backband { position: absolute; inset: 0; width: 620px; height: 400px; }
  .brand--back { left: 150px; top: 80px; text-align: left; }
  .brand--back .brand__name { font-size: 68px; color: #e6e3e3; }
  .brand--back .brand__tagline { font-size: 22px; color: #d9c4c5; letter-spacing: 1.6px; }
  .legal {
    position: absolute; left: 48px; top: 246px; font-size: 11.5px; font-weight: 300;
    color: var(--back-text); line-height: 1.5;
  }
  .website {
    position: absolute; left: 250px; top: 316px; font-size: 30px; font-weight: 400;
    color: #ffffff; letter-spacing: 0.5px;
  }
</style>
</head>
<body>
<main class="stage">
  <section class="card card--front" aria-label="Visitenkarte Vorderseite">
    <svg class="card__band" viewBox="0 0 620 120" aria-hidden="true">
      <polygon points="0,38 330,108 620,62 620,120 0,120" fill="var(--brand-red-deep)"/>
      <polygon points="0,60 330,118 620,80 620,120 0,120" fill="var(--brand-red)"/>
    </svg>
    <div class="brand">
      <div class="brand__name">Kaldora</div>
      <div class="brand__tagline">FINANCE CONSULTING</div>
    </div>
    <div class="person">
      <div class="person__name">Lukas Brenner</div>
      <div class="person__role">Geschäftsführer</div>
    </div>
    <div class="contact">
      <div class="contact__address">Birkenweg 47<br>04177 Leipzig</div>
      <div class="contact__list">
        <span class="contact__label">Mail</span><span class="contact__value">l.brenner@kaldora.de</span>
        <span class="contact__label">Tel.</span><span class="contact__value">0341 48207316</span>
        <span class="contact__label">Mobil</span><span class="contact__value">0172 5518409</span>
        <span class="contact__label">Fax</span><span class="contact__value">0341 48207399</span>
      </div>
    </div>
  </section>

  <section class="card card--back" aria-label="Visitenkarte Rückseite">
    <svg class="card__backband" viewBox="0 0 620 400" aria-hidden="true">
      <polygon points="380,0 620,0 620,400 470,400" fill="var(--brand-red-deep)" opacity="0.55"/>
      <polygon points="0,330 620,250 620,400 0,400" fill="#7e161c" opacity="0.5"/>
    </svg>
    <div class="brand brand--back">
      <div class="brand__name">Kaldora</div>
      <div class="brand__tagline">FINANCE CONSULTING</div>
    </div>
    <p class="legal">Freier Versicherungsmakler mit Erlaubnis nach § 34d GewO<br>Wirtschaftskammer Elstertal, Lindenhof 9, 04103 Markbrunn</p>
    <div class="website">kaldora.de</div>
  </section>
</main>
</body>
</html>
```